Price sign

Looking for a fresh new pricing sign.. with new prices size 2ft tall x 4ft wide , express lube $40.95, automatic transmission $129.95, radiator $109.95, Torvex plus express lube $79.95, std trans/ diff $79.95, tuneup 4cyl $149.95, 6cyl $175.95 ,

```html
<!DOCTYPE html>
<html lang="en">
<head>
<meta charset="utf-8">
<title>Revo's Service Price Sign</title>
<link href="https://fonts.googleapis.com/css2?family=Oswald:wght@500;600&family=Roboto+Condensed:wght@800;900&family=Roboto:wght@900&display=swap" rel="stylesheet">
<style>
:root{
  --red:#9d1b1f;
  --black:#0b0b0b;
  --white:#ffffff;
  --yellow:#f6cf16;
  --silver-1:#8e8e90;
  --silver-2:#f2f2f2;
  --backdrop:#e4e4e4;
  --head:"Roboto Condensed", sans-serif;
  --wide:"Roboto", sans-serif;
  --num:"Oswald", sans-serif;
}
*{box-sizing:border-box;margin:0;padding:0}
html,body{width:1200px;height:800px;overflow:hidden;background:var(--backdrop)}
.sign{position:absolute;left:40px;top:120px;width:1190px;height:595px;transform:scale(.9412);transform-origin:0 0;overflow:hidden}
.sign-bg{position:absolute;inset:0}
.el{position:absolute;display:flex;align-items:center;justify-content:center;line-height:1;text-transform:uppercase;white-space:nowrap}
.tag{clip-path:polygon(6px 0,100% 0,calc(100% - 6px) 100%,0 100%)}
.on-white{background:var(--white);color:var(--red)}
.on-black{background:var(--black);color:var(--white)}
.on-red{background:var(--red);color:var(--white)}
.head{font-family:var(--head);font-weight:900}
.wide{font-family:var(--wide);font-weight:900}
.t-white{color:var(--white)}
.t-black{color:var(--black)}
.t-red{color:var(--red)}
.t-yellow{color:var(--yellow)}
.minute-badge{background:var(--yellow);color:var(--red);font-family:var(--num);font-weight:600}
.minute-words{flex-direction:column;align-items:flex-start;font-family:var(--wide);font-weight:900}
.price{clip-path:polygon(10px 0,100% 0,calc(100% - 10px) 100%,0 100%);align-items:flex-start;font-family:var(--num);font-weight:500;padding-top:8px}
.price .num{transform:skewX(-8deg);letter-spacing:-3px}
.price .cur,.price .cents{transform:skewX(-8deg);font-size:28px;margin-top:6px}
.interval{font-family:var(--wide);font-size:9px;letter-spacing:.3px;clip-path:polygon(4px 0,100% 0,calc(100% - 4px) 100%,0 100%)}
.cyl{border:2px solid var(--white);font-family:var(--num);font-weight:500;font-size:36px;color:var(--white);transform:skewX(-8deg)}
.mini-price{font-family:var(--num);font-weight:500;align-items:flex-start;padding-top:6px}
.mini-price .num{font-size:40px;letter-spacing:-2px;transform:skewX(-8deg)}
.mini-price .cur,.mini-price .cents{font-size:13px;transform:skewX(-8deg)}

/* express lube */
.express-tag{left:135px;top:30px;width:235px;height:40px;font-size:40px}
.express-title{left:120px;top:72px;width:245px;height:78px;font-size:96px;letter-spacing:-2px}
.express-points{left:118px;top:152px;width:235px;height:26px;font-size:23px;letter-spacing:1px}
.express-price{left:383px;top:30px;width:152px;height:115px}
.express-price .num{font-size:90px}
.express-interval{left:362px;top:151px;width:151px;height:23px}

/* premium lube */
.premium-tag{left:738px;top:30px;width:235px;height:40px;font-size:34px}
.premium-title{left:728px;top:73px;width:240px;height:34px;font-size:34px}
.premium-brand{left:770px;top:110px;width:170px;height:34px;font-size:30px;color:var(--white);font-family:var(--head);font-weight:900;text-transform:none}
.premium-points{left:720px;top:152px;width:235px;height:26px;font-size:23px;letter-spacing:1px}
.premium-price{left:973px;top:30px;width:165px;height:115px}
.premium-price .num{font-size:90px}
.premium-interval{left:968px;top:151px;width:150px;height:23px}

/* automatic transmission */
.auto-tag{left:133px;top:226px;width:232px;height:42px;font-size:40px}
.auto-title{left:130px;top:272px;width:232px;height:32px;font-size:32px}
.auto-badge{left:128px;top:308px;width:75px;height:62px;font-size:58px}
.auto-words{left:208px;top:310px;width:150px;height:60px;font-size:32px}
.auto-price{left:383px;top:226px;width:152px;height:117px}
.auto-price .num{font-size:82px;letter-spacing:-6px}
.auto-interval{left:362px;top:348px;width:151px;height:23px}

/* tune up */
.tune-tag{left:713px;top:226px;width:230px;height:40px;font-size:40px}
.tune-title{left:708px;top:270px;width:232px;height:48px;font-size:52px}
.tune-badge{left:698px;top:323px;width:65px;height:48px;font-size:46px}
.tune-words{left:768px;top:325px;width:120px;height:46px;font-size:24px}
.cyl-4{left:948px;top:226px;width:87px;height:52px}
.cyl-4-price{left:1037px;top:226px;width:73px;height:52px}
.cyl-6{left:938px;top:286px;width:87px;height:54px}
.cyl-6-price{left:1028px;top:286px;width:72px;height:54px}
.tune-interval{left:930px;top:348px;width:160px;height:23px}

/* radiator */
.radiator-tag{left:135px;top:410px;width:232px;height:43px;font-size:40px}
.radiator-title{left:123px;top:453px;width:240px;height:54px;font-size:58px}
.radiator-badge{left:112px;top:510px;width:85px;height:65px;font-size:60px}
.radiator-words{left:203px;top:512px;width:150px;height:62px;font-size:32px}
.radiator-price{left:383px;top:410px;width:152px;height:118px}
.radiator-price .num{font-size:82px;letter-spacing:-6px}
.radiator-interval{left:362px;top:533px;width:151px;height:23px}

/* standard transmission */
.standard-tag{left:685px;top:410px;width:233px;height:43px;font-size:40px}
.standard-title{left:680px;top:455px;width:232px;height:24px;font-size:25px;letter-spacing:.5px}
.diff-tag{left:673px;top:485px;width:232px;height:40px;font-size:36px}
.standard-service{left:668px;top:528px;width:127px;height:30px;font-size:31px}
.standard-badge{left:798px;top:531px;width:37px;height:27px;font-size:26px}
.standard-words{left:838px;top:530px;width:65px;height:28px;font-size:13px}
.standard-price{left:932px;top:408px;width:153px;height:117px}
.standard-price .num{font-size:90px}
.standard-interval{left:912px;top:533px;width:153px;height:23px}
</style>
</head>
<body>
<main class="sign">
  <svg class="sign-bg" width="1190" height="595" viewBox="0 0 1190 595" aria-hidden="true">
    <defs>
      <linearGradient id="silver" x1="0" y1="0" x2="1" y2="0">
        <stop offset="0" stop-color="var(--silver-1)"/>
        <stop offset=".35" stop-color="var(--silver-2)"/>
        <stop offset=".7" stop-color="#d8d8d8"/>
        <stop offset="1" stop-color="var(--silver-1)"/>
      </linearGradient>
    </defs>
    <polygon points="0,0 630,0 600,213 0,213" fill="var(--red)"/>
    <polygon points="630,0 1190,0 1190,213 600,213" fill="var(--black)"/>
    <polygon points="0,213 600,213 580,382 0,382" fill="url(#silver)"/>
    <polygon points="600,213 1190,213 1190,382 580,382" fill="var(--red)"/>
    <polygon points="0,382 580,382 548,595 0,595" fill="var(--red)"/>
    <polygon points="580,382 1190,382 1190,595 548,595" fill="var(--black)"/>
    <g fill="none" stroke="var(--white)" stroke-width="2">
      <polyline points="0,173 100,173 120,48 135,48"/>
      <polyline points="605,173 700,173 722,48 738,48"/>
      <polyline points="580,372 680,372 695,248 713,248"/>
      <polyline points="0,555 100,555 115,430 135,430"/>
      <polyline points="552,555 650,555 668,432 685,432"/>
    </g>
    <polyline points="0,372 95,372 115,236 133,236" fill="none" stroke="#3a3a3a" stroke-width="2"/>
  </svg>

  <!-- Express lube -->
  <div class="el tag on-white head express-tag">Express</div>
  <div class="el wide t-white express-title">Lube</div>
  <div class="el wide t-white express-points">14 Point Service</div>
  <div class="el price on-black express-price"><span class="cur">$</span><span class="num">40.</span><span class="cents">95</span></div>
  <div class="el interval on-black express-interval">Service every 3000 miles</div>

  <!-- Premium lube -->
  <div class="el tag on-white head premium-tag">Revo's Best</div>
  <div class="el head t-white premium-title">Express Lube</div>
  <div class="el premium-brand">Torvex plus</div>
  <div class="el wide t-white premium-points">14 Point Service</div>
  <div class="el price on-red premium-price"><span class="cur">$</span><span class="num">79.</span><span class="cents">95</span></div>
  <div class="el interval on-red premium-interval">Service every 3000 miles</div>

  <!-- Automatic transmission -->
  <div class="el tag on-black head auto-tag">Automatic</div>
  <div class="el head t-black auto-title">Transmission</div>
  <div class="el minute-badge auto-badge">30</div>
  <div class="el minute-words t-red auto-words"><span>Minute</span><span>Service</span></div>
  <div class="el price on-black auto-price"><span class="cur">$</span><span class="num">129.</span><span class="cents">95</span></div>
  <div class="el interval on-black auto-interval">Service every 25000 miles</div>

  <!-- Tune up -->
  <div class="el tag on-white head tune-tag">Revo's</div>
  <div class="el tag on-white head tune-title">Tune Up</div>
  <div class="el minute-badge tune-badge">60</div>
  <div class="el minute-words t-yellow tune-words"><span>Minute</span><span>Service</span></div>
  <div class="el cyl cyl-4">4 Cyl</div>
  <div class="el mini-price on-black cyl-4-price"><span class="cur">$</span><span class="num">149.</span><span class="cents">95</span></div>
  <div class="el cyl cyl-6">6 Cyl</div>
  <div class="el mini-price on-black cyl-6-price"><span class="cur">$</span><span class="num">175.</span><span class="cents">95</span></div>
  <div class="el interval on-black tune-interval">Service every 25000 miles</div>

  <!-- Radiator -->
  <div class="el tag on-white head radiator-tag">Radiator</div>
  <div class="el wide t-white radiator-title">Service</div>
  <div class="el minute-badge radiator-badge">30</div>
  <div class="el minute-words t-yellow radiator-words"><span>Minute</span><span>Service</span></div>
  <div class="el price on-black radiator-price"><span class="cur">$</span><span class="num">109.</span><span class="cents">95</span></div>
  <div class="el interval on-black radiator-interval">Service every 25000 miles</div>

  <!-- Standard transmission / differential -->
  <div class="el tag on-white head standard-tag">Standard</div>
  <div class="el head t-white standard-title">Transmission or</div>
  <div class="el tag on-white head diff-tag">Diferential</div>
  <div class="el head t-white standard-service">Service</div>
  <div class="el minute-badge standard-badge">15</div>
  <div class="el minute-words t-yellow standard-words"><span>Minute</span><span>Service</span></div>
  <div class="el price on-red standard-price"><span class="cur">$</span><span class="num">79.</span><span class="cents">95</span></div>
  <div class="el interval on-red standard-interval">Service every 25000 miles</div>
</main>
</body>
</html>
```